Software Product Website and associated Company

We have developed a task management software that exists either in the cloud or can be installed on a customer site. Our task management software can be accessed by either a computer or a mobile device. We need a website designed like www.plovarix.com. We can provide you the content that you need. You may need to provide some stock photos. We have offices in Australia, USA and UK. We will need more than 5 pages for the website. The website would mainly provide product and solution information on our task management software. The website needs to be responsive and have a very nice user experience and user interface.

Target Market(s)

Large Companies, Government Departments and Hospitals

Industry/Entity Type

Business Software

Number of Pages Required

5+ page

Font styles to use

Requirements
Must have
• Must look similar to www.plovarix.com The website needs to be responsive and have a very nice user experience and user interface
Should not have
• The website should not be boring

```html
<!DOCTYPE html>
<html lang="en">
<head>
<meta charset="utf-8">
<title>Q Tasker – Task Management Software</title>
<link href="https://fonts.googleapis.com/css2?family=Raleway:wght@500;600;700;800&family=Open+Sans:wght@400;600&display=swap" rel="stylesheet">
<style>
:root{
  --green:#33b347;
  --blue:#3f7fc1;
  --ink:#2b2b2b;
  --muted:#666;
  --footer:#2a2a2a;
  --footer-line:#3a3a3a;
  --white:#fff;
}
*{box-sizing:border-box;margin:0;padding:0}
html,body{width:1200px;height:2560px;overflow:hidden}
body{position:relative;font-family:"Open Sans",Arial,sans-serif;color:var(--ink);background:#fff}

/* hero */
.hero{position:absolute;left:0;top:0;width:1200px;height:522px;border-top:4px solid var(--green);
  background:linear-gradient(120deg,#6a5a4c 0%,#3d3a38 35%,#5c6064 65%,#9aa0a4 100%)}
.hero-photo{position:absolute;inset:0;background:linear-gradient(180deg,rgba(0,0,0,.25),rgba(0,0,0,.35))}
.brand{position:absolute;display:flex;align-items:center;gap:10px;font-family:"Raleway",sans-serif;font-weight:700;color:var(--white)}
.brand-box{width:52px;height:52px;background:var(--blue);border:2px solid #fff}
.brand-name{font-size:24px;letter-spacing:.5px}
.nav{position:absolute;left:366px;top:30px;display:flex;align-items:center;gap:2px;font-family:"Raleway",sans-serif;font-weight:700;font-size:13px;color:#fff}
.nav a{padding:6px 9px;color:#fff;text-decoration:none;white-space:nowrap}
.nav a.active{background:var(--green)}
.nav .search{padding:6px 8px;display:flex}
.nav-rule{position:absolute;left:0;top:90px;width:1200px;height:1px;background:rgba(255,255,255,.2)}
.round-btn{position:absolute;top:20px;width:50px;height:50px;border-radius:50%;display:flex;align-items:center;justify-content:center}
.hero-title{position:absolute;left:0;top:148px;width:1200px;text-align:center;font-family:"Raleway",sans-serif;font-weight:800;font-size:37px;color:#fff}
.hero-sub{position:absolute;left:0;top:212px;width:1200px;text-align:center;font-size:15px;line-height:27px;color:#f1f1f1}
.signup{position:absolute;left:295px;top:299px;width:610px;height:99px;border:2px solid rgba(255,255,255,.85);border-radius:3px}
.signup-input{position:absolute;left:19px;top:22px;width:381px;height:51px;background:#fff;font-size:13px;color:#555;padding-left:26px;line-height:51px}
.signup-btn{position:absolute;left:409px;top:22px;width:179px;height:51px;background:var(--green);color:#fff;font-family:"Raleway",sans-serif;font-weight:800;font-size:17px;text-align:center;line-height:51px}
.dots{position:absolute;display:flex;gap:5px}
.dot{width:16px;height:16px;border-radius:50%;border:2px solid #fff}
.dot.on{background:var(--green)}

/* welcome */
.section-title{position:absolute;left:0;width:1200px;text-align:center;font-family:"Raleway",sans-serif;font-weight:700;font-size:24px}
.welcome-text{position:absolute;left:230px;top:630px;width:740px;text-align:center;font-size:12.5px;line-height:22px;color:var(--muted)}
.feature-circle{position:absolute;width:150px;height:150px;border-radius:50%;display:flex;align-items:center;justify-content:center}
.feature-circle::after{content:"";position:absolute;inset:8px;border-radius:50%;border:2px solid #fff}
.feature-label{position:absolute;width:300px;text-align:center;font-family:"Raleway",sans-serif;font-weight:700;font-size:14px}

/* stats */
.stats{position:absolute;left:0;top:961px;width:1200px;height:355px;
  background:linear-gradient(100deg,#c4a58c 0%,#8e7b6c 35%,#b89674 60%,#a47e5a 100%)}
.stats-shade{position:absolute;inset:0;background:rgba(40,30,25,.25)}
.stat{position:absolute;width:148px;height:148px;border-radius:50%;border:2px solid #fff;display:flex;align-items:center;justify-content:center;color:#fff;font-family:"Raleway",sans-serif;font-weight:700;font-size:25px}
.stat-label{position:absolute;width:260px;text-align:center;color:#fff;font-family:"Raleway",sans-serif;font-weight:700;font-size:14px}

/* features */
.feature-image{position:absolute;left:17px;top:1371px;width:601px;height:324px;border-radius:6px;
  background:linear-gradient(180deg,#e6e8ea 0%,#d4d6d8 88%,#9a9c9e 100%)}
.key-title{position:absolute;left:650px;top:1398px;font-family:"Raleway",sans-serif;font-weight:700;font-size:24px}
.key-list{position:absolute;left:650px;top:1453px;list-style:none}
.key-list li{display:flex;align-items:center;gap:12px;height:37px;font-size:12.5px;color:#555}
.tick{width:14px;height:14px;border-radius:50%;background:var(--green);display:flex;align-items:center;justify-content:center}
.read-more{position:absolute;left:650px;top:1650px;font-family:"Raleway",sans-serif;font-weight:700;font-size:12.5px;color:var(--green)}

/* testimonials */
.testimonials{position:absolute;left:0;top:1743px;width:1200px;height:268px;background:var(--green)}
.quote-circle{position:absolute;left:106px;top:1834px;width:133px;height:133px;border-radius:50%;background:#e9e9e9;display:flex;align-items:center;padding-left:28px}
.portrait{position:absolute;left:179px;top:1846px;width:108px;height:108px;border-radius:50%;border:4px solid #fff;background:linear-gradient(160deg,#dfe3e6,#8d949a)}
.quote-text{position:absolute;left:319px;top:1843px;width:780px;font-size:13px;line-height:24px;font-style:italic;color:#fff}
.quote-name{position:absolute;left:319px;top:1926px;font-family:"Raleway",sans-serif;font-weight:700;font-size:15px;color:#fff}

/* companies */
.company{position:absolute;top:2123px;width:154px;height:74px;border:1px solid #ddd;display:flex;align-items:center;justify-content:center;font-family:"Raleway",sans-serif;font-weight:700;font-size:19px;color:#333}
.arrow{position:absolute;top:2147px}

/* footer */
.footer{position:absolute;left:0;top:2246px;width:1200px;height:314px;background:var(--footer)}
.f-col{position:absolute;top:2276px}
.f-col h4{font-family:"Raleway",sans-serif;font-weight:700;font-size:16px;color:#fff;margin-bottom:13px}
.f-col li{list-style:none;font-size:12px;line-height:23.3px;color:#ddd}
.f-divider{position:absolute;top:2282px;width:1px;height:170px;background:var(--footer-line)}
.f-rule{position:absolute;left:0;top:2492px;width:1200px;height:1px;background:var(--footer-line)}
.copy{position:absolute;left:99px;top:2515px;font-size:12px;color:#ddd}
.social{position:absolute;left:960px;top:2509px;display:flex;gap:8px}
.social span{width:30px;height:30px;border-radius:50%;border:2px solid #fff}
</style>
</head>
<body>

<header class="hero">
  <div class="hero-photo" role="img" aria-label="Photo of hands using a phone beside an open laptop"></div>
  <div class="brand" style="left:99px;top:20px"><span class="brand-box"></span><span class="brand-name">Q TASKER</span></div>
  <nav class="nav">
    <a class="active">HOME</a><a>ABOUT US</a><a>PRODUCTS</a><a>FEATURES</a><a>BLOG</a><a>PRICING</a><a>CONTACT US</a>
    <a class="search"><svg width="13" height="13" viewBox="0 0 13 13"><circle cx="5.5" cy="5.5" r="4" fill="none" stroke="#fff" stroke-width="2"/><line x1="8.5" y1="8.5" x2="12" y2="12" stroke="#fff" stroke-width="2"/></svg></a>
  </nav>
  <div class="round-btn" style="left:990px;background:var(--blue)">
    <svg width="18" height="20" viewBox="0 0 18 20"><rect x="2" y="8" width="14" height="11" rx="2" fill="#fff"/><path d="M5 8V5a4 4 0 0 1 8 0v3" fill="none" stroke="#fff" stroke-width="2.4"/></svg>
  </div>
  <div class="round-btn" style="left:1050px;background:var(--green)">
    <svg width="20" height="20" viewBox="0 0 20 20"><path d="M3 17l1-4 9-9 3 3-9 9z" fill="#fff"/></svg>
  </div>
  <div class="nav-rule"></div>
  <h1 class="hero-title">TASK MANAGEMENT SOFTWARE</h1>
  <p class="hero-sub">We have developed a task management software that exists either in the cloud or can be installed on a customer site.<br>Our task management software can be accessed by either a computer or a mobile device.</p>
  <div class="signup">
    <div class="signup-input">ENTER YOUR EMAIL ADDRESS</div>
    <div class="signup-btn">GET STARTED</div>
  </div>
  <div class="dots" style="left:558px;top:473px"><span class="dot on"></span><span class="dot"></span><span class="dot"></span><span class="dot"></span></div>
</header>

<section class="welcome">
  <h2 class="section-title" style="top:574px">WELCOME TO Q TASKER</h2>
  <p class="welcome-text">We have developed a task management software that exists either in the cloud or can be installed on a customer site. Our task management software can be accessed by either a computer or a mobile device.</p>

  <div class="feature-circle" style="left:193px;top:710px;background:var(--blue)">
    <svg width="80" height="80" viewBox="0 0 80 80" fill="#fff" stroke="#fff" stroke-width="3">
      <circle cx="40" cy="40" r="11"/>
      <g stroke-linecap="round"><line x1="40" y1="40" x2="40" y2="12"/><line x1="40" y1="40" x2="40" y2="68"/><line x1="40" y1="40" x2="12" y2="40"/><line x1="40" y1="40" x2="68" y2="40"/><line x1="40" y1="40" x2="20" y2="20"/><line x1="40" y1="40" x2="60" y2="20"/><line x1="40" y1="40" x2="20" y2="60"/><line x1="40" y1="40" x2="60" y2="60"/></g>
      <circle cx="40" cy="10" r="5"/><circle cx="40" cy="70" r="5"/><circle cx="10" cy="40" r="5"/><circle cx="70" cy="40" r="5"/><circle cx="19" cy="19" r="5"/><circle cx="61" cy="19" r="5"/><circle cx="19" cy="61" r="5"/><circle cx="61" cy="61" r="5"/>
    </svg>
  </div>
  <div class="feature-label" style="left:118px;top:879px">TEAM WORK</div>

  <div class="feature-circle" style="left:522px;top:710px;background:var(--green)">
    <svg width="80" height="80" viewBox="0 0 80 80" fill="none" stroke="#fff" stroke-width="3.5" stroke-linecap="round">
      <path d="M14 52a24 24 0 0 1 44-18"/><polyline points="48,30 58,34 60,23"/>
      <circle cx="14" cy="56" r="6"/><circle cx="58" cy="55" r="10"/><polyline points="53,55 57,59 63,51"/>
    </svg>
  </div>
  <div class="feature-label" style="left:447px;top:879px">PROJECTS ON TRACK</div>

  <div class="feature-circle" style="left:857px;top:710px;background:var(--blue)">
    <svg width="80" height="80" viewBox="0 0 80 80" fill="none" stroke="#fff" stroke-width="4" stroke-linecap="round">
      <circle cx="40" cy="44" r="24"/><line x1="40" y1="10" x2="40" y2="20"/><line x1="33" y1="10" x2="47" y2="10"/>
      <line x1="40" y1="44" x2="52" y2="34"/><circle cx="40" cy="44" r="3" fill="#fff"/>
    </svg>
  </div>
  <div class="feature-label" style="left:782px;top:879px">TRACK TIME SPENT ON TASKS</div>
</section>

<section class="stats">
  <div class="stats-shade" role="img" aria-label="Photo of a hand holding a smartphone showing the task app"></div>
</section>
<h2 class="section-title" style="top:1011px;color:#fff">Q TASKER STATISTICS</h2>
<div class="stat" style="left:144px;top:1088px">1,863,800</div>
<div class="stat-label" style="left:88px;top:1252px">COMPANIES WORLDWIDE</div>
<div class="stat" style="left:401px;top:1088px">863,800</div>
<div class="stat-label" style="left:345px;top:1252px">ACTIVE USERS</div>
<div class="stat" style="left:651px;top:1088px">63,800</div>
<div class="stat-label" style="left:595px;top:1252px">PROJECTS MANAGED</div>
<div class="stat" style="left:892px;top:1088px">3,863,800</div>
<div class="stat-label" style="left:836px;top:1252px">COMPLETED TASKS</div>

<section class="features">
  <div class="feature-image" role="img" aria-label="Photo of a laptop showing the product's code inspector"></div>
  <h2 class="key-title">KEY FEATURES</h2>
  <ul class="key-list">
    <li><span class="tick"><svg width="8" height="8" viewBox="0 0 8 8"><polyline points="1,4 3,6 7,1.5" fill="none" stroke="#fff" stroke-width="1.6"/></svg></span>On the other hand, we denounce with righteous indignation and dislike.</li>
    <li><span class="tick"><svg width="8" height="8" viewBox="0 0 8 8"><polyline points="1,4 3,6 7,1.5" fill="none" stroke="#fff" stroke-width="1.6"/></svg></span>At vero eos et accusamus et iusto odio dignissimos ducimus qui blanditiis.</li>
    <li><span class="tick"><svg width="8" height="8" viewBox="0 0 8 8"><polyline points="1,4 3,6 7,1.5" fill="none" stroke="#fff" stroke-width="1.6"/></svg></span>Certain circumstances and owing to the claims of duty or the oblig</li>
    <li><span class="tick"><svg width="8" height="8" viewBox="0 0 8 8"><polyline points="1,4 3,6 7,1.5" fill="none" stroke="#fff" stroke-width="1.6"/></svg></span>On the other hand, we denounce with righteous indignation and dislike.</li>
    <li><span class="tick"><svg width="8" height="8" viewBox="0 0 8 8"><polyline points="1,4 3,6 7,1.5" fill="none" stroke="#fff" stroke-width="1.6"/></svg></span>Nemo enim ipsam voluptatem quia voluptas sit aspernatur aut odit aut fugit,</li>
  </ul>
  <div class="read-more">READ MORE &gt;&gt;</div>
</section>

<section class="testimonials" role="img" aria-label="Green band over a grid of customer portraits"></section>
<h2 class="section-title" style="top:1779px;color:#fff">TESTIMONIALS</h2>
<div class="quote-circle"><svg width="40" height="34" viewBox="0 0 40 34" fill="#c9c9c9"><path d="M0 34V18C0 8 6 2 16 0v6c-5 2-7 5-7 10h7v18zM24 34V18c0-10 6-16 16-18v6c-5 2-7 5-7 10h7v18z"/></svg></div>
<div class="portrait" role="img" aria-label="Portrait of the customer"></div>
<p class="quote-text">It is a long established fact that a reader will be distracted by the readable content of a page when looking at its layout. The point of using Lorem Ipsum is that it has a more-or-less normal distribution of letters, as opposed to using 'Content here, content here', making it look like readable English.</p>
<div class="quote-name">MARA QUILL</div>
<div class="dots" style="left:571px;top:1950px"><span class="dot on" style="background:#fff"></span><span class="dot"></span><span class="dot"></span></div>

<section class="companies">
  <h2 class="section-title" style="top:2052px">FEATURED COMPANIES</h2>
  <svg class="arrow" style="left:100px" width="12" height="22" viewBox="0 0 12 22"><polyline points="10,2 2,11 10,20" fill="none" stroke="#888" stroke-width="2"/></svg>
  <div class="company" style="left:183px">Swiftel</div>
  <div class="company" style="left:353px">Envora</div>
  <div class="company" style="left:522px">Tralvio</div>
  <div class="company" style="left:693px">Brightmast</div>
  <div class="company" style="left:862px">Kelnor Group</div>
  <svg class="arrow" style="left:1088px" width="12" height="22" viewBox="0 0 12 22"><polyline points="2,2 10,11 2,20" fill="none" stroke="#888" stroke-width="2"/></svg>
</section>

<footer class="footer"></footer>
<div class="brand" style="left:99px;top:2350px"><span class="brand-box"></span><span class="brand-name">Q TASKER</span></div>
<div class="f-divider" style="left:300px"></div>
<div class="f-col" style="left:319px"><h4>About us</h4><ul><li>Our Story</li><li>Team</li><li>Newsletters</li><li>Contact</li><li>Jobs</li><li>Help Us Grow</li></ul></div>
<div class="f-divider" style="left:432px"></div>
<div class="f-col" style="left:461px"><h4>Products</h4><ul><li>Plovarix Projects</li><li>Plovarix Desk</li><li>Plovarix Chat</li></ul></div>
<div class="f-divider" style="left:600px"></div>
<div class="f-col" style="left:625px"><h4>Links</h4><ul><li>Desktop Timer App</li><li>Cloud Suite for Business</li><li>Tablet App</li><li>Phone App</li><li>Handset App</li></ul></div>
<div class="f-divider" style="left:795px"></div>
<div class="f-col" style="left:818px"><h4>Resources</h4><ul><li>Roadmap &amp; Updates</li><li>Security</li><li>Privacy Policy</li><li>Terms of Service</li><li>Webinars</li><li>Free for Startups</li></ul></div>
<div class="f-divider" style="left:955px"></div>
<div class="f-col" style="left:978px"><h4>Legal</h4><ul><li>Certified Trainers</li><li>Plovarix</li><li>Developer Zone</li><li>Referral Program</li><li>Refund Policy</li><li>Login</li></ul></div>
<div class="f-rule"></div>
<div class="copy">Copyrights © 2016, Q Tasker. All rights reserved.</div>
<div class="social"><span></span><span></span><span></span><span></span></div>

</body>
</html>
```